Hawaii Luxury Real Estate Sales Broker needs Stationery Design Project

I am a high end property Broker here in Hawaii. I am trying to distinguish myself and my name as a brand as opposed to just being one in hundreds of Realtors out there. I am fortunate to have positioned myself into this particular market and would like to continue to grow my business here by finding the right added touch of classy detail that will make me stand out to Buyers and Sellers of this caliber. I am looking to brand myself via stationary and ads that I can place internationally. The high net worth individuals that I will be reaching out to make this a project that needs to emulate class and sophistication but with a bit of a feminine appeal as I am a woman. :-) Because I live in Hawaii I think this too may be able to play a part of the elegance in design based on the beauty that surrounds us here in the Pacific.

Target Market(s)

High Net Worth Individuals (Carrowell List, Brook Ave Ledger, Private Jet owners)

Industry/Entity Type

Business

Requirements
Must have
• My initials. I would like to see my name or initials always at their fingertips as I want them to be thinking of me as their Realtor.
Should not have
• Nothing too cheesy or touristy. It is important that this is something I can confidently send to high net worth individuals.

```html
<!DOCTYPE html>
<html lang="en">
<head>
<meta charset="utf-8">
<title>Lani Ashford Hawaiian Real Estate – Letterhead</title>
<link rel="stylesheet" href="https://fonts.googleapis.com/css2?family=Josefin+Sans:wght@100;300&display=swap">
<style>
  :root {
    --lagoon: #26d7d9;
    --lagoon-text: #2cc5ce;
    --paper: #ffffff;
    --foam: #e9fbfb;
  }
  html, body {
    margin: 0;
    padding: 0;
    overflow: hidden;
    background: var(--paper);
  }
  .letterhead {
    position: relative;
    width: 1200px;
    height: 968px;
    overflow: hidden;
    background: var(--paper);
    font-family: "Josefin Sans", "Futura", sans-serif;
    font-weight: 300;
  }
  .header-band {
    position: absolute;
    left: 30px;
    top: 28px;
    width: 1042px;
    height: 166px;
    background: var(--lagoon);
  }
  .islands-art {
    position: absolute;
    left: 745px;
    top: 34px;
  }
  .monogram,
  .brand-name,
  .contact-line,
  .footer-line {
    position: absolute;
    margin: 0;
    line-height: 1;
    white-space: nowrap;
  }
  .monogram {
    left: 50px;
    top: 48px;
    font-size: 150px;
    font-weight: 100;
    color: var(--paper);
    letter-spacing: -4px;
  }
  .brand-name {
    left: 245px;
    top: 94px;
    font-size: 45px;
    color: var(--paper);
  }
  .contact-line {
    left: 245px;
    top: 149px;
    font-size: 52px;
    color: var(--paper);
  }
  .contact-line .email {
    font-size: 44px;
    margin-left: 26px;
  }
  .flower-art {
    position: absolute;
    left: 1012px;
    top: 808px;
  }
  .footer-line {
    left: 143px;
    top: 908px;
    font-size: 40px;
    color: var(--lagoon-text);
  }
  .footer-line .footer-phone {
    margin-left: 70px;
  }
</style>
</head>
<body>
  <main class="letterhead">
    <div class="header-band"></div>

    <svg class="islands-art" width="332" height="196" viewBox="0 0 332 196" role="img" aria-label="White silhouette map of the Hawaiian island chain">
      <g fill="#ffffff" fill-opacity="0.5">
        <rect x="0" y="0" width="270" height="50" rx="14"/>
        <rect x="195" y="44" width="75" height="60" rx="14"/>
        <rect x="251" y="104" width="76" height="56" rx="14"/>
      </g>
      <rect x="251" y="160" width="76" height="34" rx="12" fill="#26d7d9"/>
    </svg>

    <p class="monogram">LA</p>
    <p class="brand-name">Lani Ashford Hawaiian Real Estate</p>
    <p class="contact-line"><span class="phone">555 555 5555</span><span class="email">email@domain.com</span></p>

    <svg class="flower-art" width="186" height="158" viewBox="0 0 186 158" role="img" aria-label="Turquoise hibiscus flower illustration">
      <defs>
        <radialGradient id="flowerTone" cx="0.55" cy="0.55" r="0.6">
          <stop offset="0" stop-color="#26d7d9"/>
          <stop offset="0.7" stop-color="#5fdfe1"/>
          <stop offset="1" stop-color="#e9fbfb"/>
        </radialGradient>
      </defs>
      <rect x="0" y="0" width="186" height="158" rx="36" fill="url(#flowerTone)"/>
    </svg>

    <p class="footer-line"><span class="footer-name">Lani Ashford Real Estate</span><span class="footer-phone">555 555 5555</span></p>
  </main>
</body>
</html>
```